Tilda Tinkerwire, An IT Company Has New Logo, Need Fresh Business Cards

IT company is called Tilda Tinkerwire and is displayed nicely with the new logo from here on pitchloft. Would like a fresh business card look that encompasses the idea that we want clients to Cherish Every Gadget. I love the use of circuitry with hearts as endpoints and x's and o's. It needs to have room for my certification logos of which there are 4 and a BRJ Alumni log. I am attaching my current card to illustrate how it has always captured attention, but that was in the early stages of business when I was doing more residential work. I am focused on businesses now, so a level of professionalism is necessary. I would also like the card to lend itself well to additional stationary, email signature, ticketing template for my workboard, etc. For the time being, I need the card for an upcoming conference so that work will come later. Color scheme should be that of the new logo. Thank you and I look forward to the designs.

Target Market(s)

Businesses looking for IT services.

Industry/Entity Type

Information Technology

Contact Information for Business Card

See above

Requirements
Must have
• New logo colors and a warm feel. Possibly a tad feminine as I am female, but appealing to males.
Nice to have
• I would like techy, but no too much so. I like friendly and connecting feels. People LOVED my old card and called me because it gave them a warm feeling.

```html
<!DOCTYPE html>
<html lang="en">
<head>
<meta charset="utf-8">
<title>Tilda Tinkerwire – Business Card</title>
<link href="https://fonts.googleapis.com/css2?family=Open+Sans:wght@400;600;700&family=PT+Sans+Narrow:wght@700&display=swap" rel="stylesheet">
<style>
  :root {
    --backdrop: #2b2b2b;
    --card-white: #ffffff;
    --ink: #4a4a4a;
    --ink-soft: #555555;
    --sky: #85c9e8;
    --lime: #b7d86a;
    --pink: #e07ab8;
    --badge: #a9daf0;
  }
  * { margin: 0; padding: 0; box-sizing: border-box; }
  html, body { width: 1200px; height: 960px; overflow: hidden; }
  body { background: var(--backdrop); position: relative; font-family: "Open Sans", Arial, sans-serif; }

  .card {
    position: absolute; left: 300px; top: 310px;
    width: 600px; height: 342px;
    background: var(--card-white);
    border-radius: 18px; overflow: hidden;
  }
  .brand-dot {
    position: absolute; left: 116px; top: 82px;
    width: 74px; height: 74px; border-radius: 50%;
    background: var(--sky);
  }
  .brand-name {
    position: absolute; left: 0; width: 306px; top: 170px;
    text-align: center; font-size: 26px; line-height: 30px; font-weight: 600;
    color: var(--sky); letter-spacing: -.3px; white-space: nowrap;
  }
  .tagline {
    position: absolute; left: 0; width: 306px; top: 196px;
    text-align: center; font-size: 9px; line-height: 12px; font-weight: 600;
    color: var(--pink); letter-spacing: 2.6px; text-transform: uppercase; white-space: nowrap;
  }
  .divider {
    position: absolute; left: 289px; top: 73px;
    width: 1px; height: 137px; background: var(--ink);
  }
  .contact { position: absolute; left: 316px; top: 71px; color: var(--ink); white-space: nowrap; }
  .contact .call { font-size: 18px; font-weight: 600; line-height: 24px; }
  .contact .phone { font-size: 19px; font-weight: 600; line-height: 26px; }
  .contact .web, .contact .email { font-size: 17px; line-height: 23px; color: var(--ink-soft); }
  .contact .web { margin-top: 5px; }
  .services {
    margin-top: 12px; font-family: "PT Sans Narrow", "Arial Narrow", sans-serif;
    font-size: 19px; line-height: 25px; font-weight: 700; color: var(--ink);
    display: flex; align-items: center; gap: 5px;
  }
  .services .dot { width: 7px; height: 7px; border-radius: 50%; background: var(--sky); }

  .credential-band {
    position: absolute; left: 0; bottom: 0; width: 600px; height: 82px;
    background: var(--sky); border-top: 3px solid var(--lime);
  }
  .badge {
    position: absolute; top: 20px; height: 36px;
    background: var(--badge); border-radius: 4px;
  }
</style>
</head>
<body>
  <div class="card">
    <div class="brand-dot" aria-hidden="true"></div>
    <div class="brand-name">Tilda Tinkerwire</div>
    <div class="tagline">Cherish Every Gadget</div>

    <div class="divider"></div>

    <div class="contact">
      <div class="call">Call Tilda!</div>
      <div class="phone">407-555-0186</div>
      <div class="web">www.tilda-tinkerwire.com</div>
      <div class="email">tilda.tinkerwire@mailnest.com</div>
      <div class="services">Desktops<span class="dot"></span>Laptops<span class="dot"></span>Tablets</div>
    </div>

    <div class="credential-band">
      <div class="badge" style="left:28px;width:84px"></div>
      <div class="badge" style="left:136px;width:64px"></div>
      <div class="badge" style="left:222px;width:106px"></div>
      <div class="badge" style="left:349px;width:66px"></div>
      <div class="badge" style="left:426px;width:80px"></div>
      <div class="badge" style="left:516px;width:56px"></div>
    </div>
  </div>
</body>
</html>
```